Catering Menu Package

I currently have a complete menu package, which we have redesigned as far as content, now I need to it put together in a catalog type format. It is essentially 10-12 pages in length, and will be sent for print production. Upon receiving a final edit
Updates

I have added an example gif to the project.

I did this free hand this basically what I am looking for. please change text and type to whatever you think would look best. This is a total rough design so, feel free to change any and everything. The text for the page is on the word documents. If you need more images let me know I am in the process of getting as many images uploaded for your use.

Reason: I figured we got a late jump with questions, so i am extending a few days .

Target Market(s)

The target market is business who wish to have catered luncheons, breakfasts , meetings

Industry/Entity Type

Catering

Requirements
Must have
• I have attached a copy of the text that what we want in the package, our logo, and i have also attached a catering package of another company to give you an idea what the finished product will be
Should not have
• It should not look identical to the example catering packages, these are for some inspiration we want our own design with the same type of look and feel

```html
<!DOCTYPE html>
<html lang="en">
<head>
<meta charset="utf-8">
<title>Entrée Salads – Larkspur Table Co.</title>
<link href="https://fonts.googleapis.com/css2?family=Great+Vibes&family=Alegreya:wght@400&display=swap" rel="stylesheet">
<style>
  :root {
    --paper: #efe9df;
    --paper-deep: #e6ddd0;
    --ink: #2a2420;
    --title-ink: #1e1a17;
    --melon: #efd9a8;
    --berry: #d9412e;
    --cantaloupe: #f09a4a;
    --honeydew: #c9dca0;
    --grass: #6f8d3a;
    --badge-bg: #f7f3ee;
  }
  * { margin: 0; padding: 0; box-sizing: border-box; }
  html, body { width: 1200px; height: 928px; overflow: hidden; background: #fff; }
  .page { position: relative; width: 1200px; height: 928px; overflow: hidden; }
  .menu-panel {
    position: absolute; left: 0; top: 0;
    width: 774px; height: 928px;
    background: radial-gradient(ellipse at 45% 45%, var(--paper) 0%, var(--paper-deep) 100%);
  }
  .menu-title {
    position: absolute;
    left: 300px; width: 446px;
    top: 46px;
    text-align: right;
    font-family: "Great Vibes", cursive;
    font-weight: 400;
    font-size: 46px;
    line-height: 52px;
    color: var(--title-ink);
    white-space: nowrap;
  }
  .salad-list {
    position: absolute;
    left: 116px; top: 111px;
    width: 630px;
    font-family: "Alegreya", serif;
    font-size: 17.6px;
    line-height: 21.2px;
    color: var(--ink);
  }
  .salad-name { text-align: right; }
  .salad-desc { text-align: right; text-align-last: left; }
  .salad-price { text-align: right; }
  .salad.spaced { margin-top: 24px; }
  .salad-desc.closing { text-align-last: right; }
  .photo {
    position: absolute; left: 774px; top: 0;
    width: 426px; height: 928px;
    background:
      radial-gradient(circle at 30% 18%, var(--melon) 0%, rgba(239,217,168,0) 35%),
      radial-gradient(circle at 55% 45%, var(--melon) 0%, rgba(239,217,168,0) 28%),
      radial-gradient(circle at 35% 70%, var(--berry) 0%, rgba(217,65,46,0) 30%),
      radial-gradient(circle at 80% 65%, var(--cantaloupe) 0%, rgba(240,154,74,0) 35%),
      radial-gradient(circle at 85% 40%, var(--honeydew) 0%, rgba(201,220,160,0) 30%),
      linear-gradient(180deg, #e6b58a 0%, #d9935a 45%, #c9553b 70%, var(--grass) 100%);
  }
  .brand {
    position: absolute;
    left: 1066px; top: 730px;
    width: 100px;
    display: flex; flex-direction: column; align-items: center; gap: 8px;
  }
  .brand-mark { width: 80px; height: 80px; border-radius: 50%; background: var(--badge-bg); }
  .brand-name {
    font-family: "Alegreya", serif;
    font-size: 14px; line-height: 16px;
    color: var(--badge-bg);
    text-align: center;
  }
</style>
</head>
<body>
<div class="page">
  <section class="menu-panel">
    <h1 class="menu-title">Entrée Salads</h1>
    <div class="salad-list">
      <div class="salad">
        <p class="salad-name">California Cobb-</p>
        <p class="salad-desc">Spring Mix topped with House Roasted Turkey Breast, Applewood Smoked Bacon Bits, Diced Tomatoes, Avocado Slices, Roasted Red Peppers, and Kalamata Olives.</p>
        <p class="salad-price">$&amp;.&amp;&amp;</p>
      </div>
      <div class="salad spaced">
        <p class="salad-name">Titanic-</p>
        <p class="salad-desc">Iceberg wedge topped with Diced Tomatoes, Applewood Smoked Bacon Bits and our House-made Bleu Cheese Dressing.</p>
        <p class="salad-price">$&amp;.&amp;&amp;</p>
      </div>
      <div class="salad">
        <p class="salad-name">LTC Chef Salad-</p>
        <p class="salad-desc">House Roasted Turkey Breast, Black Forest Ham. American and Swiss Cheeses, diced Tomatoes served over Crisp Romaine Lettuce.</p>
        <p class="salad-price">$&amp;.&amp;&amp;</p>
      </div>
      <div class="salad">
        <p class="salad-name">Grilled Chicken and Organic Spinach-</p>
        <p class="salad-desc">Grilled Chicken Breast strips served over Organic Baby Spinach topped with Crum&shy;bled Gorgonazola Cheese, Julienne Red Onions, Button Mushroom Slices, and Garlic Croutons.</p>
        <p class="salad-price">$&amp;.&amp;&amp;</p>
      </div>
      <div class="salad">
        <p class="salad-name">Bistro Steak Salad-</p>
        <p class="salad-desc">grilled Bistro Tenderloin served over Spring Mix topped with Sliced Button Mush&shy;rooms, Red Onions, Shredded Carrots, Grape Tomatoes, Crumbled Gorgonzola Cheese, and Walnut Halves.</p>
        <p class="salad-price">$&amp;.&amp;&amp;</p>
      </div>
      <div class="salad">
        <p class="salad-name">Grilled Vegetable Salad-</p>
        <p class="salad-desc">BalsamicMarinated Grilled Vegetables served over Spring Mix with Avocado slices, Feta Cheese, and Pepperoncinis.</p>
        <p class="salad-price">$&amp;.&amp;&amp;</p>
      </div>
      <div class="salad">
        <p class="salad-name">Micro Power Green Salad-</p>
        <p class="salad-desc">Blend of Micro Spinach, Kale, Chard and Arugala, topped with Goat Cheese, Oven Roasted Beets, Almond Slivers, Julienne Carrots and finished with a House-made Shitake-Sesame Vinaigrette.</p>
        <p class="salad-price">$&amp;.&amp;&amp;</p>
      </div>
      <div class="salad">
        <p class="salad-name">Powerhouse Salad-</p>
        <p class="salad-desc closing">Spring Mix Lettuces topped with a generous scoop of Tuna Salad, Egg Whites, Shredded Carrots, Cucumbers, Grape Tomatoes, and Broccoli Florets.</p>
      </div>
    </div>
  </section>
  <div class="photo" role="img" aria-label="Photo of a catered fruit display: skewered melon, strawberries and pineapple over diced watermelon, cantaloupe and honeydew"></div>
  <div class="brand">
    <div class="brand-mark"></div>
    <p class="brand-name">Larkspur Table Co.</p>
  </div>
</div>
</body>
</html>
```